Life Coaching Business - needs business card design with logo

I need a business card and logo design for a life coaching business I started based in Los Angeles. I offer services to clients that wish to bring more balance and overall wholeness to their lives. As of right now, the business name is "Marcus Elwood Coaching." An iidea I had for the logo was to be kind of a Yin-Yang symbol but with dolphins, as the dolphin has symbolic meaning for my business. Although I am really open to other ideas as long as it incorporates the idea of “balance,” “wholeness,” and “dolphins.”I also wanted to incorporate the color blue, maybe in the form of water, waves, or some sort of peaceful imagery.

```html
<!DOCTYPE html>
<html lang="en">
<head>
<meta charset="utf-8">
<title>Marcus Elwood Coaching – Business Card</title>
<link href="https://fonts.googleapis.com/css2?family=Open+Sans:wght@400;600&display=swap" rel="stylesheet">
<style>
  :root {
    --backdrop: #3a3a3c;
    --card-dark: #121213;
    --card-mid: #2a2a2c;
    --text-white: #f2f2f2;
    --accent-cyan: #4fd3df;
    --icon-blue: #5aa9d6;
    --mark-blue: #6fb8d8;
  }
  * { margin: 0; padding: 0; box-sizing: border-box; }
  html, body { width: 1200px; height: 716px; overflow: hidden; }
  body {
    background: var(--backdrop);
    font-family: "Open Sans", Arial, sans-serif;
    color: var(--text-white);
    position: relative;
  }
  .card {
    position: absolute;
    top: 209px;
    width: 520px;
    height: 298px;
    border-radius: 4px;
    overflow: hidden;
    box-shadow: 0 10px 30px rgba(0,0,0,0.45);
  }
  .card--front { left: 50px; }
  .card--back { left: 630px; }
  .card__texture {
    position: absolute; inset: 0;
    background: radial-gradient(ellipse at 40% 35%, var(--card-mid), var(--card-dark) 75%);
  }
  .brand-mark {
    position: absolute;
    display: flex; align-items: center; gap: 10px;
  }
  .brand-mark__dot {
    width: 22px; height: 22px; border-radius: 50%;
    background: var(--mark-blue);
  }
  .brand-mark__name {
    font-size: 17px; font-weight: 400; color: var(--mark-blue);
  }
  .card--front .brand-mark { left: 50%; top: 96px; transform: translateX(-50%); }
  .card--back .brand-mark { right: 34px; bottom: 44px; }
  .business-name {
    position: absolute;
    font-size: 22px; font-weight: 400; letter-spacing: 0.3px;
    color: var(--text-white);
  }
  .card--front .business-name { left: 0; right: 0; text-align: center; top: 168px; }
  .card--back .business-name { right: 34px; top: 30px; }
  .contact { position: absolute; left: 40px; top: 104px; }
  .contact__name {
    font-size: 22px; color: var(--accent-cyan); margin-bottom: 12px;
  }
  .contact__row {
    display: flex; align-items: center; gap: 8px;
    font-size: 15px; margin-bottom: 6px;
  }
  .contact__icon { width: 16px; height: 16px; flex: none; }
</style>
</head>
<body>
  <section class="card card--front">
    <div class="card__texture" role="img" aria-label="Dark card surface covered with water droplets"></div>
    <div class="brand-mark">
      <span class="brand-mark__dot"></span>
      <span class="brand-mark__name">Marcus Elwood Coaching</span>
    </div>
    <p class="business-name">Marcus Elwood Coaching.</p>
  </section>

  <section class="card card--back">
    <div class="card__texture" role="img" aria-label="Dark card surface covered with water droplets"></div>
    <p class="business-name">Marcus Elwood Coaching.</p>
    <div class="contact">
      <p class="contact__name">Jonah Pryce</p>
      <p class="contact__row">
        <svg class="contact__icon" viewBox="0 0 16 16" aria-hidden="true">
          <rect width="16" height="16" rx="2" fill="var(--icon-blue)"/>
          <path d="M5 3.5h2l.8 2.5-1.2.9a6 6 0 0 0 2.5 2.5l.9-1.2 2.5.8v2c0 .6-.5 1-1 1A8 8 0 0 1 4 4.5c0-.6.4-1 1-1z" fill="#fff"/>
        </svg>
        <span>021 5550192</span>
      </p>
      <p class="contact__row">
        <svg class="contact__icon" viewBox="0 0 16 16" aria-hidden="true">
          <rect width="16" height="16" rx="2" fill="var(--icon-blue)"/>
          <rect x="3" y="4.5" width="10" height="7" fill="none" stroke="#fff" stroke-width="1.2"/>
          <path d="M3 4.5l5 4 5-4" fill="none" stroke="#fff" stroke-width="1.2"/>
        </svg>
        <span>jpryce@elwoodcoach.com</span>
      </p>
    </div>
    <div class="brand-mark">
      <span class="brand-mark__dot"></span>
      <span class="brand-mark__name">Marcus Elwood Coaching</span>
    </div>
  </section>
</body>
</html>
```